Business card design needed

We design, manufacture and install kitchen robes vanity etc.
We have a current card that i want to upload that you can base the design around and make suggestions for other design but we need the logo to be unchanged that i will up load along with our current card.

Industry/Entity Type

Business

Contact Information for Business Card

Tallowind Joinery Works
Dorian Calvestri
47 Quarrington Avenue, Kelbrook S.A 5099
dorian@tallowindjoinery.com.au
Lic. No. Bld 582904 Bld 740251

```html
<!DOCTYPE html>
<html lang="en">
<head>
<meta charset="utf-8">
<title>Tallowind Joinery Works – Business Card</title>
<link rel="stylesheet" href="https://fonts.googleapis.com/css2?family=Jost:wght@400;500;600&display=swap">
<style>
  :root {
    --lime: #86c21a;
    --slate: #9daeb1;
    --ink: #111111;
    --paper: #ffffff;
    --edge: #8a8a8a;
  }
  html, body {
    margin: 0;
    padding: 0;
    width: 1200px;
    height: 1170px;
    overflow: hidden;
    background: var(--paper);
  }
  .sheet {
    position: relative;
    width: 1200px;
    height: 1170px;
  }
  .card {
    position: absolute;
    left: 240px;
    width: 729px;
    height: 425px;
    display: block;
  }
  .card--front { top: 103px; }
  .card--back { top: 651px; }
  .card-edge { fill: var(--paper); stroke: var(--edge); stroke-width: 1; }
  .shape-lime { fill: var(--lime); }
  .shape-slate { fill: var(--slate); }
  .holder-name {
    font-family: "Jost", sans-serif;
    font-weight: 400;
    font-size: 36px;
    fill: var(--paper);
  }
  .contact-line {
    font-family: "Jost", sans-serif;
    font-weight: 400;
    font-size: 14.5px;
    fill: var(--paper);
  }
  .company-name {
    font-family: "Jost", sans-serif;
    font-weight: 600;
    font-size: 17px;
    letter-spacing: 0.3px;
    fill: var(--slate);
  }
  .headline {
    font-family: "Jost", sans-serif;
    font-weight: 400;
    font-size: 50px;
    fill: var(--paper);
  }
  .service-item {
    font-family: "Jost", sans-serif;
    font-weight: 400;
    font-size: 19px;
    fill: var(--ink);
  }
  .service-bullet { fill: var(--lime); }
</style>
</head>
<body>
<main class="sheet">

  <!-- Front of card -->
  <svg class="card card--front" viewBox="175 75 532 310" xmlns="http://www.w3.org/2000/svg">
    <defs>
      <clipPath id="front-clip"><rect x="175" y="75" width="532" height="310"/></clipPath>
    </defs>
    <rect class="card-edge" x="175" y="75" width="532" height="310"/>
    <g clip-path="url(#front-clip)">
      <polygon class="shape-lime" points="175,75 200,75 251.5,126.5 175,203"/>
      <polygon class="shape-lime" points="213,75 328,75 598,345 558,385 523,385"/>
      <polygon class="shape-slate" points="458,75 512,75 707,270 707,385 652,385 400,133"/>
      <circle class="shape-lime" cx="640" cy="75" r="38"/>
      <polygon class="shape-lime" points="590,195 707,78 707,150 626,231"/>
    </g>

    <text class="holder-name" transform="translate(445 117) rotate(45)">Dorian Calvestri</text>

    <text class="contact-line" transform="translate(345 117) rotate(45)">47 Quarrington Avenue, Kelbrook S.A 5099</text>
    <text class="contact-line" transform="translate(326 132) rotate(45)">dorian@tallowindjoinery.com.au</text>
    <text class="contact-line" transform="translate(309 148) rotate(45)">Lic. No. Bld 582904 Bld 740251</text>

    <rect class="shape-lime" x="240" y="148" width="9" height="9"/>
    <text class="company-name" transform="translate(215 170) rotate(45)">TALLOWIND JOINERY WORKS</text>
  </svg>

  <!-- Back of card -->
  <svg class="card card--back" viewBox="175 475 532 310" xmlns="http://www.w3.org/2000/svg">
    <defs>
      <clipPath id="back-clip"><rect x="175" y="475" width="532" height="310"/></clipPath>
    </defs>
    <rect class="card-edge" x="175" y="475" width="532" height="310"/>
    <g clip-path="url(#back-clip)">
      <polygon class="shape-lime" points="258,475 303,475 348,520 175,693 175,558"/>
      <polygon class="shape-lime" points="317,475 423,475 693,745 640,798 170,328"/>
      <polygon class="shape-slate" points="550,475 707,632 707,740 497,530"/>
      <circle class="shape-lime" cx="720" cy="485" r="22"/>
      <polygon class="shape-lime" points="687,600 707,580 707,620"/>
    </g>

    <text class="headline" transform="translate(400 516) rotate(45)">Custom made</text>

    <g class="service-list">
      <circle class="service-bullet" cx="352" cy="551" r="4"/>
      <text class="service-item" transform="translate(359 556) rotate(45)">Kitchens</text>
      <circle class="service-bullet" cx="335" cy="569" r="4"/>
      <text class="service-item" transform="translate(342 574) rotate(45)">Vanities</text>
      <circle class="service-bullet" cx="318" cy="587" r="4"/>
      <text class="service-item" transform="translate(325 592) rotate(45)">Laundry</text>
      <circle class="service-bullet" cx="300" cy="605" r="4"/>
      <text class="service-item" transform="translate(307 610) rotate(45)">Robes</text>
      <circle class="service-bullet" cx="283" cy="623" r="4"/>
      <text class="service-item" transform="translate(290 628) rotate(45)">Entertainment units</text>
      <circle class="service-bullet" cx="266" cy="641" r="4"/>
      <text class="service-item" transform="translate(273 646) rotate(45)">Flat packs</text>
    </g>
  </svg>

</main>
</body>
</html>
```